Looking for a cool, modern Cannabis Jar Label

I want you to come up with a better, modern look for a label.

I need it sized to 4” x 3” - I plan to print directly to label printer.

I want you to use Photoshop and deliver me a layered PSD file that I can edit and modify the information as needed..

The label information will need to include places for:
(1) Strain Name - most important part of label - larger font size than rest - example Marlow Frost, KTV #7, Copperleaf Haze
(2) Pricing - for Gram, 1/8, 1/4, 1/2. and Ounce
(3) Strain Designation (Hybrid, Indica or Sativa) - maybe color coded, different color for Indica v. Sativa, just an idea
(4) THC and CBD percentages - for example 23% THC and 0.05% CBD
(5) Farm name - a place where we can add the name/logo of the business that produced the product. example - Bramwell Farms

I have attached a simple mockup showing the information.

I have also attached a few samples of labels we like to give you an idea of the look and feel we are going for.

I am wanting a very clean, modern, classy, readable look.The font will use is Gotham Font.

HI Everyone! Thank you for all of your designs. I am requesting an extension because I need more time to give adequate feedback to the designers. Thank you for your participation and all of your efforts! I will be making a decision soon!

• Gotham Font

Designer to choose colors to be used in the design.

• Thank you for your designs. I am sorry i have been slow in providing feedback, things have been really busy around here!
• I wanted to give some group general feedback. After reviewing all of the designs, there is a common theme among all of the designs that I would like to see changed.
• I would like to see the per gram pricing more prominent on the label. This is what most people are looking for when they are purchasing the product. So I would like to see this stand out from the other pricing tiers. As I think about it, they don't all need to be grouped together in a line. You could have the Per Gram pricing front and center some where and then the other pricing tiers grouped together somewhere else on the label.
• This is the order of importance of items on the label. Items at the the top of the list should be bigger than those below it.
• 1. Strain name
• 2. Pricing - being per gram the most important of all prices
• 3. THC/CBD percentages
• 4. Strain Type (indica, sativa, hybrid)
• 5. Farm name/logo
• When laying out these labels, they will be going on rounded jars and they will be on display. Think of jars with fancy labels in a candy store. They need to be eye catchy, appealing, but easy read.
• Thank you for all of your hard work, everyone is doing a great job.
• Best,
• Nadia

```html
<!DOCTYPE html>
<html lang="en">
<head>
<meta charset="utf-8">
<title>Strain Jar Labels — Indica, Hybrid, Sativa</title>
<link rel="stylesheet" href="https://fonts.googleapis.com/css2?family=Montserrat:wght@300;400;500;700;800;900&display=swap">
<style>
  :root {
    --ink: #111111;
    --paper: #ffffff;
    --backdrop: #f1f1f1;
    --indica: #3bb54a;
    --hybrid: #3a55a4;
    --sativa: #ed2224;
    --rule: 6px;
  }
  * { box-sizing: border-box; margin: 0; padding: 0; }
  html, body {
    width: 1200px; height: 1200px; overflow: hidden;
    background: var(--backdrop);
    font-family: "Montserrat", sans-serif;
    color: var(--ink);
  }
  .sheet { position: relative; width: 1200px; height: 1200px; }

  .label {
    position: absolute;
    width: 516px; height: 386px;
    background: var(--paper);
    box-shadow: 0 2px 10px rgba(0,0,0,0.12);
  }
  .label--indica { left: 64px;  top: 192px; --accent: var(--indica); }
  .label--hybrid { left: 620px; top: 192px; --accent: var(--hybrid); }
  .label--sativa { left: 358px; top: 611px; --accent: var(--sativa); }

  /* potency band */
  .potency { position: absolute; left: 0; top: 0; width: 516px; height: 128px; }
  .potency svg { position: absolute; inset: 0; }
  .strain-type {
    position: absolute; left: 0; top: 0; width: 160px; height: 128px;
    display: flex; align-items: center; justify-content: center;
    color: var(--paper); font-weight: 900; font-size: 30px; letter-spacing: 1px;
    padding-left: 4px;
  }
  .reading { position: absolute; top: 0; height: 128px; text-align: center; }
  .reading--thc { left: 180px; width: 150px; }
  .reading--cbd { left: 340px; width: 176px; }
  .reading__name {
    display: block; margin-top: 6px;
    font-weight: 300; font-size: 22px; letter-spacing: 8px; padding-left: 8px;
  }
  .reading__value {
    display: block; margin-top: 8px;
    font-weight: 900; font-size: 37px; color: var(--accent);
  }

  .rule { position: absolute; left: 0; width: 516px; height: var(--rule); background: var(--ink); }
  .rule--top { top: 128px; }
  .rule--mid { top: 254px; }

  /* price tiers: per-gram leads, larger */
  .prices {
    position: absolute; left: 0; top: 134px; width: 516px; height: 120px;
    display: flex; align-items: center;
  }
  .tier { position: relative; height: 90px; padding-left: 6px; }
  .tier + .tier { border-left: 1.5px solid var(--ink); }
  .tier--gram { width: 152px; padding-left: 12px; }
  .tier--bulk { width: 91px; }
  .tier__size { display: block; font-size: 15px; font-weight: 400; line-height: 1; margin-top: 4px; }
  .tier__price {
    display: block; margin-top: 22px;
    font-size: 30px; font-weight: 500; letter-spacing: 0.5px; line-height: 1; white-space: nowrap;
  }
  .tier__price small { font-size: 16px; font-weight: 700; letter-spacing: 0; margin-right: 1px; }
  .tier--gram .tier__size { font-size: 17px; font-weight: 700; }
  .tier--gram .tier__price { margin-top: 10px; font-size: 54px; font-weight: 800; letter-spacing: 1px; }
  .tier--gram .tier__price small { font-size: 26px; font-weight: 800; }

  /* identity row */
  .identity { position: absolute; left: 0; top: 260px; width: 516px; height: 126px; display: flex; }
  .farm {
    width: 128px; height: 108px; margin-top: 9px; flex: none;
    border-right: 1.5px solid var(--ink);
    display: flex; align-items: center; justify-content: center; gap: 6px;
  }
  .farm__dot { width: 28px; height: 28px; border: 2px solid var(--ink); border-radius: 50%; flex: none; }
  .farm__name { font-size: 11px; font-weight: 800; line-height: 1.15; letter-spacing: 0.5px; }
  .strain-name {
    flex: 1; display: flex; align-items: center; justify-content: center; text-align: center;
    font-size: 40px; font-weight: 800; letter-spacing: 2px; line-height: 1.25;
    text-transform: uppercase; padding: 0 6px;
  }
</style>
</head>
<body>
<main class="sheet">

  <section class="label label--indica">
    <div class="potency">
      <svg width="516" height="128" viewBox="0 0 516 128" aria-hidden="true">
        <polygon points="0,0 190,0 162,128 0,128" fill="var(--indica)"/>
        <line x1="190" y1="0" x2="163" y2="128" stroke="var(--ink)" stroke-width="6"/>
        <line x1="353" y1="0" x2="326" y2="128" stroke="var(--ink)" stroke-width="6"/>
      </svg>
      <div class="strain-type">INDICA</div>
      <div class="reading reading--thc"><span class="reading__name">THC</span><span class="reading__value">23%</span></div>
      <div class="reading reading--cbd"><span class="reading__name">CBD</span><span class="reading__value">0.05%</span></div>
    </div>
    <div class="rule rule--top"></div>
    <div class="prices">
      <div class="tier tier--gram"><span class="tier__size">g.</span><span class="tier__price"><small>$</small>10</span></div>
      <div class="tier tier--bulk"><span class="tier__size">1/8</span><span class="tier__price"><small>$</small>35</span></div>
      <div class="tier tier--bulk"><span class="tier__size">1/4</span><span class="tier__price"><small>$</small>70</span></div>
      <div class="tier tier--bulk"><span class="tier__size">1/2</span><span class="tier__price"><small>$</small>140</span></div>
      <div class="tier tier--bulk"><span class="tier__size">o.z</span><span class="tier__price"><small>$</small>280</span></div>
    </div>
    <div class="rule rule--mid"></div>
    <div class="identity">
      <div class="farm"><span class="farm__dot"></span><span class="farm__name">BRAMWELL<br>FARMS</span></div>
      <h2 class="strain-name">Amber Creek<br>Chill</h2>
    </div>
  </section>

  <section class="label label--hybrid">
    <div class="potency">
      <svg width="516" height="128" viewBox="0 0 516 128" aria-hidden="true">
        <polygon points="0,0 190,0 162,128 0,128" fill="var(--hybrid)"/>
        <line x1="190" y1="0" x2="163" y2="128" stroke="var(--ink)" stroke-width="6"/>
        <line x1="353" y1="0" x2="326" y2="128" stroke="var(--ink)" stroke-width="6"/>
      </svg>
      <div class="strain-type">HYBRID</div>
      <div class="reading reading--thc"><span class="reading__name">THC</span><span class="reading__value">23%</span></div>
      <div class="reading reading--cbd"><span class="reading__name">CBD</span><span class="reading__value">0.05%</span></div>
    </div>
    <div class="rule rule--top"></div>
    <div class="prices">
      <div class="tier tier--gram"><span class="tier__size">g.</span><span class="tier__price"><small>$</small>10</span></div>
      <div class="tier tier--bulk"><span class="tier__size">1/8</span><span class="tier__price"><small>$</small>35</span></div>
      <div class="tier tier--bulk"><span class="tier__size">1/4</span><span class="tier__price"><small>$</small>70</span></div>
      <div class="tier tier--bulk"><span class="tier__size">1/2</span><span class="tier__price"><small>$</small>140</span></div>
      <div class="tier tier--bulk"><span class="tier__size">o.z</span><span class="tier__price"><small>$</small>280</span></div>
    </div>
    <div class="rule rule--mid"></div>
    <div class="identity">
      <div class="farm"><span class="farm__dot"></span><span class="farm__name">BRAMWELL<br>FARMS</span></div>
      <h2 class="strain-name">Amber Creek<br>Chill</h2>
    </div>
  </section>

  <section class="label label--sativa">
    <div class="potency">
      <svg width="516" height="128" viewBox="0 0 516 128" aria-hidden="true">
        <polygon points="0,0 190,0 162,128 0,128" fill="var(--sativa)"/>
        <line x1="190" y1="0" x2="163" y2="128" stroke="var(--ink)" stroke-width="6"/>
        <line x1="353" y1="0" x2="326" y2="128" stroke="var(--ink)" stroke-width="6"/>
      </svg>
      <div class="strain-type">SATIVA</div>
      <div class="reading reading--thc"><span class="reading__name">THC</span><span class="reading__value">23%</span></div>
      <div class="reading reading--cbd"><span class="reading__name">CBD</span><span class="reading__value">0.05%</span></div>
    </div>
    <div class="rule rule--top"></div>
    <div class="prices">
      <div class="tier tier--gram"><span class="tier__size">g.</span><span class="tier__price"><small>$</small>10</span></div>
      <div class="tier tier--bulk"><span class="tier__size">1/8</span><span class="tier__price"><small>$</small>35</span></div>
      <div class="tier tier--bulk"><span class="tier__size">1/4</span><span class="tier__price"><small>$</small>70</span></div>
      <div class="tier tier--bulk"><span class="tier__size">1/2</span><span class="tier__price"><small>$</small>140</span></div>
      <div class="tier tier--bulk"><span class="tier__size">o.z</span><span class="tier__price"><small>$</small>280</span></div>
    </div>
    <div class="rule rule--mid"></div>
    <div class="identity">
      <div class="farm"><span class="farm__dot"></span><span class="farm__name">BRAMWELL<br>FARMS</span></div>
      <h2 class="strain-name">Amber Creek<br>Chill</h2>
    </div>
  </section>

</main>
</body>
</html>
```